Attention grabbing 6x9 postcard

We are looking to have an attention grabbing post card that be sent out to homeowners from our roofing company Vell Roofing. the concept is that on the front it will say something like (STOP THE KNOCKING!
Tired of roofers knocking on your door? Contact us because we value your time as much as you value the roof over your head."
Vell Roofing
VellRoofing.com
877.602.VELL
info@vellroofing.com

Please feel free to come up with something very creative. Once we pick the final design we will provide the copy.

```html
<!DOCTYPE html>
<html lang="en">
<head>
<meta charset="utf-8">
<title>Vell Roofing Postcard</title>
<link rel="stylesheet" href="https://fonts.googleapis.com/css2?family=Montserrat:wght@400;500;600;700;800;900&display=swap">
<style>
  :root {
    --page-bg: #eeeeee;
    --card-white: #ffffff;
    --ink: #1e1e1f;
    --panel-dark: #232326;
    --honey: #e9b234;
    --honey-deep: #d99f22;
    --text-light: #ffffff;
    --photo-sky: #e6eef5;
    --photo-roof: #9a6a55;
    --photo-brick: #c9785a;
    --photo-shirt: #141414;
    --shingle-grey: #6d7178;
  }
  * { box-sizing: border-box; margin: 0; padding: 0; }
  html, body {
    width: 1200px; height: 1200px; overflow: hidden;
    background: var(--page-bg);
    font-family: "Montserrat", sans-serif;
  }
  .postcard {
    position: absolute; left: 222px; width: 755px; height: 510px;
    overflow: hidden; background: var(--card-white);
  }
  .postcard--front { top: 64px; }
  .postcard--back { top: 626px; }

  /* Front */
  .front-photo {
    position: absolute; inset: 0;
    background:
      linear-gradient(90deg, rgba(255,255,255,0.95) 0%, rgba(255,255,255,0.55) 28%, rgba(255,255,255,0) 55%),
      linear-gradient(180deg, rgba(255,255,255,1) 0%, rgba(255,255,255,0.7) 30%, rgba(255,255,255,0) 55%),
      linear-gradient(90deg, var(--photo-roof) 0%, var(--photo-roof) 48%, var(--photo-shirt) 56%, var(--photo-shirt) 80%, var(--photo-brick) 92%),
      var(--photo-sky);
  }
  .front-brand {
    position: absolute; left: 0; width: 385px; top: 196px;
    text-align: center; color: var(--honey);
    font-weight: 600; font-size: 31px; letter-spacing: 5px;
  }
  .headline { position: absolute; left: 20px; color: var(--ink); font-weight: 900; line-height: 1; }
  .headline__stop { top: 282px; font-size: 124px; letter-spacing: -5px; }
  .headline__the { top: 388px; left: 148px; font-size: 47px; font-weight: 800; letter-spacing: -1px; }
  .headline__knocking { top: 438px; left: 24px; font-size: 52px; font-weight: 800; letter-spacing: -2.5px; }

  /* Back */
  .back-shapes { position: absolute; inset: 0; }
  .tired-band { position: absolute; left: 0; top: 30px; width: 380px; height: 120px; }
  .tired-title {
    position: absolute; left: 23px; top: 50px; color: var(--ink);
    font-weight: 800; line-height: 1;
  }
  .tired-title__big { display: block; font-size: 40px; letter-spacing: -0.5px; }
  .tired-title__small { display: block; font-size: 24px; font-weight: 700; margin-top: 4px; }
  .value-copy {
    position: absolute; left: 23px; top: 164px; width: 420px;
    color: var(--text-light); font-size: 17.5px; font-weight: 500; line-height: 1.4;
  }
  .services { position: absolute; left: 24px; top: 226px; display: flex; gap: 10px; }
  .service { width: 90px; display: flex; flex-direction: column; align-items: center; }
  .service__hex { width: 90px; height: 115px; }
  .service__label {
    margin-top: 8px; width: 90px; height: 39px; border-radius: 6px;
    display: flex; align-items: center; justify-content: center; text-align: center;
    font-size: 11.5px; font-weight: 700; line-height: 1.15; color: var(--ink);
  }
  .service__label--honey { background: var(--honey); }
  .service__label--white { background: var(--card-white); }
  .back-brand {
    position: absolute; left: 23px; top: 412px; color: var(--honey);
    font-size: 35px; font-weight: 700; line-height: 1.12;
  }
  .contact-list { position: absolute; left: 208px; top: 414px; list-style: none; }
  .contact-list li {
    display: flex; align-items: center; gap: 10px; height: 28px;
    color: var(--text-light); font-size: 16px; font-weight: 500;
  }
  .contact-list svg { width: 16px; height: 16px; }
  .stamp-box {
    position: absolute; left: 620px; top: 23px; width: 111px; height: 73px;
    border: 1.2px solid var(--ink);
  }
  .mail-brand {
    position: absolute; left: 580px; width: 165px; top: 470px; text-align: center;
    color: var(--ink); font-size: 15px; font-weight: 700; letter-spacing: 2.5px;
  }
</style>
</head>
<body>

<section class="postcard postcard--front">
  <div class="front-photo" role="img" aria-label="Photo of a man in glasses and a black turtleneck holding up his hand in a stop gesture, in front of a house with a roof under construction"></div>
  <div class="front-brand">VELL ROOFING</div>
  <div class="headline headline__stop">STOP</div>
  <div class="headline headline__the">THE</div>
  <div class="headline headline__knocking">KNOCKING!</div>
</section>

<section class="postcard postcard--back">
  <svg class="back-shapes" viewBox="0 0 755 510" aria-hidden="true">
    <polygon points="0,0 492,0 436,182 494,510 0,510" fill="var(--honey)"/>
    <polygon points="0,0 484,0 426,180 458,510 0,510" fill="var(--panel-dark)"/>
  </svg>

  <svg class="tired-band" viewBox="0 0 380 120" aria-hidden="true">
    <polygon fill="var(--card-white)" points="0,8 22,12 40,6 70,13 100,6 130,12 170,4 200,11 230,5 262,13 290,3 320,10 345,2 372,6 360,60 366,118 330,110 300,116 262,108 230,116 196,109 160,117 128,110 96,118 60,110 30,117 0,112"/>
    <polygon fill="var(--honey)" points="0,14 24,18 42,12 72,19 102,12 132,18 172,10 202,17 232,11 264,19 292,9 322,16 345,9 362,12 352,60 356,110 330,103 300,109 262,101 230,109 196,102 160,110 128,103 96,111 60,103 30,110 0,105"/>
  </svg>
  <h2 class="tired-title">
    <span class="tired-title__big">Tired of roofers</span>
    <span class="tired-title__small">knocking on your door?</span>
  </h2>

  <p class="value-copy">Contact us because we value your time as much as you value the roof over your head.</p>

  <div class="services">
    <div class="service">
      <svg class="service__hex" viewBox="0 0 90 115" role="img" aria-label="Photo of a home gable with grey shingle roof">
        <polygon points="45,0 90,26 90,80 45,106 0,80 0,26" fill="#8a8378"/>
        <polygon points="0,84 45,110 90,84 90,94 45,115 0,94" fill="var(--honey)"/>
      </svg>
      <div class="service__label service__label--honey">Retail/<br>Commercial</div>
    </div>
    <div class="service">
      <svg class="service__hex" viewBox="0 0 90 115" role="img" aria-label="Photo of storm-damaged asphalt shingles">
        <polygon points="45,0 90,26 90,80 45,106 0,80 0,26" fill="var(--shingle-grey)"/>
        <polygon points="0,84 45,110 90,84 90,94 45,115 0,94" fill="var(--card-white)"/>
      </svg>
      <div class="service__label service__label--white">Storm<br>Damage</div>
    </div>
    <div class="service">
      <svg class="service__hex" viewBox="0 0 90 115" role="img" aria-label="Photo of a newly built dark shingle roof">
        <polygon points="45,0 90,26 90,80 45,106 0,80 0,26" fill="#55585e"/>
        <polygon points="0,84 45,110 90,84 90,94 45,115 0,94" fill="var(--honey)"/>
      </svg>
      <div class="service__label service__label--honey">New<br>Construction</div>
    </div>
    <div class="service">
      <svg class="service__hex" viewBox="0 0 90 115" role="img" aria-label="Photo of a roof covered with a blue tarp awaiting repair">
        <polygon points="45,0 90,26 90,80 45,106 0,80 0,26" fill="#6f8aa6"/>
        <polygon points="0,84 45,110 90,84 90,94 45,115 0,94" fill="var(--card-white)"/>
      </svg>
      <div class="service__label service__label--white">Repairs &amp;<br>Restoration</div>
    </div>
  </div>

  <div class="back-brand">Vell<br>Roofing</div>

  <ul class="contact-list">
    <li>
      <svg viewBox="0 0 24 24" aria-hidden="true"><path d="M6.6 10.8a15 15 0 0 0 6.6 6.6l2.2-2.2a1 1 0 0 1 1-.25 11.4 11.4 0 0 0 3.6.57 1 1 0 0 1 1 1V20a1 1 0 0 1-1 1A17 17 0 0 1 3 4a1 1 0 0 1 1-1h3.5a1 1 0 0 1 1 1c0 1.25.2 2.45.57 3.57a1 1 0 0 1-.25 1z" fill="none" stroke="#fff" stroke-width="1.8"/></svg>
      877.602.VELL
    </li>
    <li>
      <svg viewBox="0 0 24 24" aria-hidden="true"><g fill="none" stroke="#fff" stroke-width="1.6"><circle cx="12" cy="12" r="9"/><ellipse cx="12" cy="12" rx="4" ry="9"/><path d="M3 12h18M4.5 7.5h15M4.5 16.5h15"/></g></svg>
      VellRoofing.com
    </li>
    <li>
      <svg viewBox="0 0 24 24" aria-hidden="true"><path d="M22 3 2 11l7 2.5L12 21l3-6 7-12zM9 13.5 22 3" fill="#fff" stroke="#fff" stroke-width="1.2" stroke-linejoin="round"/></svg>
      info@vellroofing.com
    </li>
  </ul>

  <div class="stamp-box" aria-hidden="true"></div>
  <div class="mail-brand">VELL ROOFING</div>
</section>

</body>
</html>
```